Dental Bridgeway Company Needs Design for Table top Display at Tradeshows

We need a Graphic Design for a Table Top Display that is used at Trade-shows we attend.
A little bit about what we do: We are a Dental Transitions company, we help new and retiring dentists buy or sell their dental practices. Think of it as a real-estate broker for Dental businesses. Some of the things that Transitions include are practice valuations, which is a determination of how much that practice is worth in respect the the amount of business that comes through on a yearly basis. We also help dentists find associates, or help new graduates find associateships.
KMV Dental Crossings was founded by Martin L. Okafor, whom is an attorney in the dental field, who brings a new perspective to the dental transition experience due to his legal background.
About the project: We have a table top display called an Voru TK-4 (Spec sheet attatched, but don't worry, the printers will do all the cutting and printing..but this will let you see how the actual display is divided, however, the image should be one cohesive image), it consists of 5 (3 main and two very small side) panels made from vinyl. Here are the approx. specs of the display.
Height: 1.51 m
59.5''
Width: 2.44 m
96''
Depth: 0.52 m
20.4''
Our printers request Vector graphics or EPS, and the color mode must be Pantone / PMS Spot Color
What we would like to see: We need our company logo, motto "We are here to guide you through"
Colors: Deep Burgundy, White, Grey, and Black
A list of our services: Practice Sales, Buyer Representation, Seller Representation, Practice Valuations, Associateships
We need the font to be large and clear, easy to read, because people are going to be walking by this display, you need to be able to read it quick! We are open to creative design Ideas!
View our website to see more about out and our general marketing image: www.okaforclinicguides.example
Please add in www.kmvcrossings.example to the image (this website is not live yet but will be soon)
Our sliders were accidentally incorrect, the design slider was all the way to "feminine" but we need the design to appeal to both men, and women equally. It has been updated. Thank you
Target Market(s)
Our market is largely retiring dentists, and also new dentists looking to start.
Industry/Entity Type
Marketing
Requirements
Must have
- Must have company logo, name, motto, website and list of services.
Services are: Practice Valuations, Practice Sales, Buyer Representation, Seller Representation, Associateships.
Please remake logo into vector format as well to go along with the vector format (but keep it as close to the original as possible)
Should not have
- No teeth please :)

```html
<!DOCTYPE html>
<html lang="en">
<head>
<meta charset="utf-8">
<title>KMV Dental Crossings – Table Top Display</title>
<link rel="stylesheet" href="https://fonts.googleapis.com/css2?family=Libre+Franklin:wght@400;500;600&display=swap">
<style>
  :root {
    --burgundy: #3c121e;
    --charcoal: #414042;
    --ink: #2a1016;
    --text-grey: #444444;
    --frame: #cfcfcf;
    --white: #ffffff;
    --map-tone: #f2f2f2;
  }
  html, body {
    margin: 0;
    padding: 0;
    width: 1200px;
    height: 1000px;
    overflow: hidden;
    background: var(--white);
    font-family: "Libre Franklin", Arial, sans-serif;
  }
  .display {
    position: absolute;
    left: 36px;
    top: 199px;
    width: 1126px;
    height: 566px;
    border: 1px solid var(--frame);
    background: var(--white);
  }
  .brand-bar {
    position: absolute;
    left: 0; top: 0;
    width: 100%;
    height: 156px;
  }
  .brand-name {
    position: absolute;
    left: 187px;
    top: 58px;
    margin: 0;
    font-size: 37px;
    font-weight: 600;
    letter-spacing: 0.5px;
    color: var(--ink);
    white-space: nowrap;
  }
  .motto {
    position: absolute;
    left: 624px;
    top: 91px;
    margin: 0;
    font-size: 21px;
    font-weight: 400;
    color: var(--text-grey);
  }
  .services-band {
    position: absolute;
    left: 0; top: 156px;
    width: 100%;
    height: 301px;
    background: var(--burgundy);
  }
  .coverage-map {
    position: absolute;
    left: 194px;
    top: 35px;
    width: 380px;
    height: 235px;
    border-radius: 6px;
    background: linear-gradient(135deg, var(--white), var(--map-tone));
  }
  .services {
    position: absolute;
    left: 622px;
    top: 28px;
    color: var(--white);
  }
  .services-title {
    margin: 0 0 20px;
    font-size: 38px;
    font-weight: 500;
  }
  .services-list {
    margin: 0;
    padding: 0;
    list-style: none;
    font-size: 28px;
    line-height: 33px;
  }
  .services-list li::before {
    content: "•";
    display: inline-block;
    width: 26px;
  }
  .accent-stripe {
    position: absolute;
    left: 0; top: 501px;
    width: 100%;
    height: 10px;
    background: var(--burgundy);
  }
  .footer-bar {
    position: absolute;
    left: 0; top: 511px;
    width: 100%;
    height: 55px;
    background: var(--charcoal);
  }
  .website {
    position: absolute;
    left: 624px;
    top: 14px;
    margin: 0;
    font-size: 22px;
    color: var(--white);
  }
</style>
</head>
<body>
  <div class="display">
    <header class="brand-bar">
      <h1 class="brand-name">KMV Dental Crossings</h1>
      <p class="motto">We are here to guide you through</p>
    </header>

    <section class="services-band">
      <div class="coverage-map" role="img" aria-label="Map of the United States showing state outlines"></div>
      <div class="services">
        <h2 class="services-title">Our Services</h2>
        <ul class="services-list">
          <li>Practice Valuations</li>
          <li>Practice Sales</li>
          <li>Buyer Representation</li>
          <li>Seller Representation</li>
          <li>Associateships</li>
        </ul>
      </div>
    </section>

    <div class="accent-stripe"></div>
    <footer class="footer-bar">
      <p class="website">www.kmvcrossings.example</p>
    </footer>
  </div>
</body>
</html>
```